Geschäftspapiere für Lasergravuren
Zielgruppe
Lasergravuren z.B. auf Glas, Holz, Filz, Papier, Acryl, eloxierten Aluminium zu Dekorationszwecken,
Ausschneiden von Elementen z.B. aus Holz, Filz, Papier, Acryl usw. zu Dekorationszwecken mit dem Lasergravierer.
Anfertigung verschiedener Dekorationsartikel,
Zielgruppe: Frauen (mit Familien) aller Altersgruppen, die Freude am Dekorieren und Verschenken haben
Aufgabenstellung
Das vorhandene Logo soll mit eingebunden werden

```html
<!DOCTYPE html>
<html lang="de">
<head>
<meta charset="utf-8">
<title>Lunaris Laserdeko – Geschäftsausstattung</title>
<link href="https://fonts.googleapis.com/css2?family=Open+Sans:wght@400;600&display=swap" rel="stylesheet">
<style>
  :root{
    --gold:#ad8a45;
    --gold-line:#d9a84e;
    --icon:#e0a040;
    --grey:#707070;
    --ink:#1f2f4f;
    --paper:#ffffff;
    --bg:#ffffff;
  }
  *{box-sizing:border-box;margin:0;padding:0}
  html,body{width:1200px;height:1200px;overflow:hidden;background:var(--bg);font-family:"Open Sans",sans-serif;color:var(--ink)}
  .canvas{position:relative;width:1200px;height:1200px}
  .sheet{position:absolute;background:var(--paper);box-shadow:5px 6px 6px rgba(0,0,0,.45)}
  .abs{position:absolute}
  .brand{position:absolute;display:flex;flex-direction:column;align-items:center;color:var(--grey);font-weight:400;line-height:1}
  .brand .mark{border:2px solid var(--grey);border-radius:50%}
  .contact{position:absolute;font-size:7px;line-height:1.35;color:var(--ink)}
  .contact .row{display:flex;align-items:flex-start;gap:6px;position:absolute;left:0;white-space:nowrap}
  .contact svg{width:10px;height:10px;flex:none;fill:var(--icon)}
  .gold-rule{position:absolute;height:4px;background:var(--gold-line)}
  .web{position:absolute;display:flex;align-items:center;gap:12px;font-size:9px;color:var(--ink);white-space:nowrap}
  .web svg{width:9px;height:9px;fill:none;stroke:var(--icon);stroke-width:1.2}
  .photo{position:absolute}
  .p-wood{background:linear-gradient(160deg,#c2783f,#8c4a22)}
  .p-crowns{background:linear-gradient(90deg,#d9a0a8,#8d87a8 35%,#3f8a78 55%,#e6dcc8 80%,#b08a70)}
  .p-glass{background:linear-gradient(180deg,#2b2b2b,#111 60%,#3a3a3a)}
  .p-lace{background:linear-gradient(120deg,#2b3d63,#4d6590 60%,#b9c0c8)}
  .marker{position:absolute;width:0;height:0;border-top:5px solid transparent;border-bottom:5px solid transparent;border-left:6px solid var(--icon)}
</style>
</head>
<body>
<svg width="0" height="0" style="position:absolute">
  <symbol id="i-home" viewBox="0 0 10 10"><path d="M5 1 0 5.5h1.4V9h2.6V6.5h2V9h2.6V5.5H10z"/></symbol>
  <symbol id="i-phone" viewBox="0 0 10 10"><path d="M2 .8 3.8 2.6 2.9 3.7c.7 1.5 1.9 2.7 3.4 3.4l1.1-.9L9.2 8 8 9.2C4.2 8.8 1.2 5.8.8 2z"/></symbol>
  <symbol id="i-fax" viewBox="0 0 10 10"><path d="M2.5 1h5v2.5h-5zM1 4h8v4H7.5v1h-5V8H1zm2.5 3.5v1h3v-1z"/></symbol>
  <symbol id="i-mail" viewBox="0 0 10 10"><path d="M.5 3 5 .5 9.5 3v6h-9zm1 .6V8h7V3.6L5 6z"/></symbol>
  <symbol id="i-web" viewBox="0 0 10 10"><circle cx="5" cy="5" r="4"/><path d="M1 5h8M5 1c-2 2.5-2 5.5 0 8M5 1c2 2.5 2 5.5 0 8"/></symbol>
</svg>

<main class="canvas">

  <!-- Briefbogen -->
  <section class="sheet letterhead" style="left:42px;top:42px;width:508px;height:716px">
    <div class="abs" style="left:0;top:0;width:508px;height:8px;background:var(--grey)"></div>
    <div class="brand" style="left:174px;top:20px;width:160px">
      <span class="mark" style="width:38px;height:38px"></span>
      <span style="font-size:34px;margin-top:6px">Lunaris</span>
    </div>
    <div class="contact" style="left:374px;top:104px">
      <div class="row" style="top:0"><svg><use href="#i-home"/></svg><span style="font-weight:600">Lindenweg 12</span></div>
      <div class="row" style="top:10px;left:16px"><span>12345 Musterstadt</span></div>
      <div class="row" style="top:28px"><svg><use href="#i-phone"/></svg><span>01234 - 56 789</span></div>
      <div class="row" style="top:45px"><svg><use href="#i-fax"/></svg><span>Telefax&nbsp; 01234 - 56 780</span></div>
      <div class="row" style="top:62px"><svg><use href="#i-mail"/></svg><span>info@lunaris-deko.de</span></div>
    </div>
    <span class="marker" style="left:14px;top:245px"></span>
    <span class="marker" style="left:14px;top:486px"></span>
    <div class="gold-rule" style="left:0;top:633px;width:508px"></div>
    <div class="photo p-wood"   style="left:19px;top:644px;width:28px;height:47px" role="img" aria-label="Gravierte Holz-Handyhülle"></div>
    <div class="photo p-crowns" style="left:58px;top:644px;width:56px;height:47px" role="img" aria-label="Gelaserte Teelichthalter in Pastellfarben"></div>
    <div class="photo p-glass"  style="left:124px;top:644px;width:47px;height:47px" role="img" aria-label="Gravierte Weingläser"></div>
    <div class="photo p-lace"   style="left:179px;top:644px;width:65px;height:47px" role="img" aria-label="Gravierte Spitzenmuster auf Filz"></div>
    <div class="photo p-wood"   style="left:255px;top:644px;width:26px;height:47px" role="img" aria-label="Gravierte Holz-Handyhülle"></div>
    <div class="photo p-crowns" style="left:292px;top:644px;width:59px;height:47px" role="img" aria-label="Gelaserte Teelichthalter in Pastellfarben"></div>
    <div class="photo p-glass"  style="left:360px;top:644px;width:46px;height:47px" role="img" aria-label="Gravierte Weingläser"></div>
    <div class="photo p-lace"   style="left:414px;top:644px;width:65px;height:47px" role="img" aria-label="Gravierte Spitzenmuster auf Filz"></div>
    <div class="web" style="left:172px;top:697px"><svg><use href="#i-web"/></svg><span>www.lunaris-laserdeko.de</span></div>
  </section>

  <!-- Kuvert Rückseite -->
  <section class="sheet envelope-back" style="left:597px;top:162px;width:559px;height:282px">
    <svg class="abs" style="left:0;top:0" width="559" height="82" viewBox="0 0 559 82">
      <path d="M0 0H559L532 70Q527 80 514 80H45Q32 80 27 70Z" fill="var(--gold)"/>
    </svg>
    <span class="abs" style="left:247px;top:17px;width:44px;height:44px;border-radius:50%;border:2px solid #fff"></span>
  </section>

  <!-- Kuvert Vorderseite -->
  <section class="sheet envelope-front" style="left:597px;top:478px;width:559px;height:280px">
    <div class="brand" style="left:34px;top:24px;width:150px">
      <span class="mark" style="width:40px;height:40px"></span>
      <span style="font-size:34px;margin-top:6px">Lunaris</span>
    </div>
    <div class="abs" style="right:24px;top:230px;font-size:8.5px;display:flex;align-items:center;gap:5px;white-space:nowrap">
      <svg style="width:11px;height:11px;fill:var(--icon)"><use href="#i-home"/></svg>
      <span>Lindenweg 12</span>
      <span style="width:5px;height:5px;border-radius:50%;background:var(--icon)"></span>
      <span>12345 Musterstadt</span>
    </div>
    <div class="gold-rule" style="left:0;top:248px;width:559px"></div>
    <div class="web" style="left:197px;top:260px"><svg><use href="#i-web"/></svg><span>www.lunaris-laserdeko.de</span></div>
  </section>

  <!-- Visitenkarte Logo -->
  <section class="sheet card card-logo" style="left:39px;top:897px;width:359px;height:231px">
    <div class="brand" style="left:79px;top:46px;width:200px">
      <span class="mark" style="width:86px;height:86px;border-color:var(--gold)"></span>
      <span style="font-size:52px;margin-top:8px">Lunaris</span>
    </div>
  </section>

  <!-- Visitenkarte Kontakt -->
  <section class="sheet card card-contact" style="left:424px;top:897px;width:358px;height:231px">
    <div class="photo p-wood"   style="left:23px;top:23px;width:31px;height:55px" role="img" aria-label="Gravierte Holz-Handyhülle"></div>
    <div class="photo p-crowns" style="left:67px;top:23px;width:72px;height:55px" role="img" aria-label="Gelaserte Teelichthalter in Pastellfarben"></div>
    <div class="photo p-glass"  style="left:23px;top:90px;width:46px;height:45px" role="img" aria-label="Gravierte Weingläser"></div>
    <div class="photo p-lace"   style="left:77px;top:90px;width:65px;height:45px" role="img" aria-label="Gravierte Spitzenmuster auf Filz"></div>
    <div class="photo p-lace"   style="left:23px;top:152px;width:65px;height:46px" role="img" aria-label="Gravierte Spitzenmuster auf Filz"></div>
    <div class="photo p-glass"  style="left:95px;top:152px;width:47px;height:46px" role="img" aria-label="Gravierte Weingläser"></div>
    <div class="brand" style="left:210px;top:23px;width:120px">
      <span class="mark" style="width:34px;height:34px"></span>
      <span style="font-size:26px;margin-top:4px">Lunaris</span>
    </div>
    <div class="abs" style="left:200px;top:91px;width:140px;text-align:center;font-size:11.5px;color:var(--ink)">Jonas Wellmer</div>
    <div class="contact" style="left:220px;top:130px">
      <div class="row" style="top:0"><svg><use href="#i-home"/></svg><span style="font-weight:600">Lindenweg 12</span></div>
      <div class="row" style="top:10px;left:16px"><span>12345 Musterstadt</span></div>
      <div class="row" style="top:29px"><svg><use href="#i-phone"/></svg><span>01234 - 56 789</span></div>
      <div class="row" style="top:46px"><svg><use href="#i-fax"/></svg><span>Telefax&nbsp; 01234 - 56 780</span></div>
      <div class="row" style="top:62px"><svg><use href="#i-mail"/></svg><span>info@lunaris-deko.de</span></div>
    </div>
    <div class="gold-rule" style="left:0;top:206px;width:358px"></div>
    <div class="web" style="left:120px;top:216px;font-size:6.5px;gap:8px"><svg style="width:7px;height:7px"><use href="#i-web"/></svg><span>www.lunaris-laserdeko.de</span></div>
  </section>

  <!-- Visitenkarte Rückseite -->
  <section class="sheet card card-back" style="left:811px;top:897px;width:359px;height:231px;background:var(--gold)">
    <span class="abs" style="left:99px;top:35px;width:160px;height:160px;border-radius:50%;border:2px solid #fff"></span>
    <span class="abs" style="left:0;top:98px;width:359px;text-align:center;font-size:30px;color:#fff;line-height:1">Lunaris</span>
  </section>

</main>
</body>
</html>
```